Business Card Design, including supply of raw art files plus a vector diagram of the zelvon logo and

We need the business card design for a company that is launching a new exciting product. The brief requires the submission of the following once the final design is chosen:

- business card layout including raw files
- a composite vector image file of the zelvon logo and tag line
- a standalone vector image file of the zelvon logo

The product will be launched as a customer engagement app.

It has 4 core modules which enables a person to do multiple things - book tours and activities, order takeaways, search for local deals and offers. A universal currency is at the heart of this product. When you use the app, you earn cashback rewards when shopping or buying at any of the merchant partners across the modules as . These rewards can then be used as full or part payment when buying goods or services at these merchant partners.

The business card must help us build the brand, communicate the benefit of the brand's key focus - the ability to earn and burn this universal cashback ccurrency - across the 4 modules - booking of tours and activities, ordering, searching for local deals and payment.

We would like the design to use the brand's blue colour the hex colour is: 00
Dark grey : 646464
Darker blue shadow: 058bdd
Main Blue: 0084ff

We need to translate this into a CMYK print or spot colour print.

Both print options to be supplied as separate files.

An example of the base concept we have in mind is attached for your reference.

The font used by the brand is Proxima Nova.

Note: the duration has been set as 2 days.

Industry/Entity Type

Business

Contact Information for Business Card

Carla Mendoza
Marketing
W: www.zelvon.example
M: + 61 400555123
T: +61 2 5550 1473
A: Suite 7, Level 2, 14-18 Harwick Street, Sydney, NSW, 2000, Australia

Font styles to use
Sans Serif

Requirements
Must have
• zelVon logo and tagline
• address details
• zelVon icons as supplied
Nice to have
• would like to have the option of a spot varnish layer over the logo and icons at the back of the card

```html
<!DOCTYPE html>
<html lang="en">
<head>
<meta charset="utf-8">
<title>zelVon business card</title>
<link rel="stylesheet" href="https://fonts.googleapis.com/css2?family=Montserrat:wght@300;400;600;700&display=swap">
<style>
  :root {
    --brand-blue: #2f88cf;
    --logo-blue: #3d9ad8;
    --dark-grey: #4a4a4a;
    --rule-grey: #3c3c3c;
    --paper: #ffffff;
    --backdrop: #2b2b2d;
  }
  * { box-sizing: border-box; margin: 0; padding: 0; }
  html, body { width: 1200px; height: 900px; overflow: hidden; }
  body {
    background: var(--backdrop);
    font-family: "Montserrat", sans-serif;
    position: relative;
  }
  .card {
    position: absolute;
    left: 300px;
    width: 600px;
    height: 343px;
    border-radius: 22px;
    background: var(--paper);
    overflow: hidden;
    box-shadow: 0 14px 30px rgba(0,0,0,0.45);
  }
  .card-front { top: 70px; }
  .card-back { top: 487px; }

  /* Front */
  .front-mark {
    position: absolute;
    left: 205px; top: 82px;
    width: 176px; height: 176px;
    border-radius: 50%;
    background: var(--logo-blue);
    display: flex; align-items: center; justify-content: center;
    color: var(--paper);
    font-weight: 600;
    font-size: 30px;
  }
  .module-row {
    position: absolute;
    right: 24px; bottom: 22px;
    display: flex; gap: 10px; align-items: flex-end;
  }
  .module {
    display: flex; flex-direction: column; align-items: center; gap: 3px;
  }
  .module svg { width: 22px; height: 22px; display: block; }
  .module-label {
    font-size: 5px; font-weight: 600; letter-spacing: 0.3px;
    color: var(--dark-grey);
  }

  /* Back */
  .brand-lockup {
    position: absolute;
    left: 110px; top: 62px;
    display: flex; align-items: center; gap: 14px;
  }
  .brand-circle {
    width: 96px; height: 96px; border-radius: 50%;
    background: var(--logo-blue);
  }
  .brand-text { display: flex; flex-direction: column; }
  .brand-name {
    font-weight: 300; font-size: 58px; line-height: 1;
    color: var(--dark-grey); letter-spacing: 1px;
  }
  .brand-tagline {
    font-weight: 300; font-size: 17px; color: var(--dark-grey);
    margin-left: 40px; letter-spacing: 0.5px;
  }
  .info-band {
    position: absolute; left: 0; right: 0; bottom: 0;
    height: 158px;
    background: var(--brand-blue);
    border-top: 4px solid var(--rule-grey);
    color: var(--paper);
  }
  .person {
    position: absolute; right: 330px; top: 22px;
    text-align: right;
  }
  .person-name { font-weight: 700; font-size: 21px; }
  .person-role { font-weight: 400; font-size: 13px; margin-top: 1px; }
  .person-address { font-weight: 400; font-size: 12.5px; line-height: 1.45; margin-top: 14px; }
  .divider {
    position: absolute; left: 290px; top: 18px;
    width: 1px; height: 110px; background: rgba(255,255,255,0.8);
  }
  .contact-list {
    position: absolute; left: 308px; top: 18px;
    list-style: none;
    font-size: 12.5px; line-height: 1.6;
  }
  .contact-list li { display: flex; align-items: center; gap: 9px; }
  .contact-list svg { width: 11px; height: 11px; flex: none; }
  .contact-list strong { font-weight: 700; }
</style>
</head>
<body>
  <section class="card card-front" aria-label="Card front">
    <div class="front-mark">zelVon</div>
    <div class="module-row">
      <div class="module">
        <svg viewBox="0 0 22 22"><circle cx="11" cy="11" r="8" fill="none" stroke="#3d9ad8" stroke-width="2.5"/><circle cx="11" cy="11" r="3.5" fill="#3d9ad8"/></svg>
        <span class="module-label">REWARDS</span>
      </div>
      <div class="module">
        <svg viewBox="0 0 22 22"><rect x="2" y="2" width="18" height="18" fill="#3d9ad8"/></svg>
        <span class="module-label">TOURS</span>
      </div>
      <div class="module">
        <svg viewBox="0 0 22 22"><rect x="2" y="6" width="18" height="13" rx="2" fill="#3d9ad8"/><rect x="7" y="3" width="8" height="4" fill="#3d9ad8"/><circle cx="11" cy="12.5" r="3.5" fill="#fff"/></svg>
        <span class="module-label">ORDERS</span>
      </div>
      <div class="module">
        <svg viewBox="0 0 22 22"><path d="M4 3l14 16M18 3L4 19" stroke="#3d9ad8" stroke-width="2.4"/></svg>
        <span class="module-label">OFFERS</span>
      </div>
      <div class="module">
        <svg viewBox="0 0 22 22"><rect x="2" y="2" width="18" height="18" fill="#3d9ad8"/></svg>
        <span class="module-label">PAY</span>
      </div>
    </div>
  </section>

  <section class="card card-back" aria-label="Card back">
    <div class="brand-lockup">
      <div class="brand-circle"></div>
      <div class="brand-text">
        <span class="brand-name">zelVon</span>
        <span class="brand-tagline">earn and spend anywhere</span>
      </div>
    </div>
    <div class="info-band">
      <div class="person">
        <div class="person-name">Carla Mendoza</div>
        <div class="person-role">Marketing</div>
        <div class="person-address">Suite 7, Level 2, 14-18 Harwick Street<br>Sydney, NSW, 2000, Australia</div>
      </div>
      <div class="divider"></div>
      <ul class="contact-list">
        <li><svg viewBox="0 0 11 11"><rect x="2.5" y="0.5" width="6" height="10" rx="1" fill="none" stroke="#fff"/></svg><span>+ 61 400555123</span></li>
        <li><svg viewBox="0 0 11 11"><path d="M2 1l2 0 1 3-1.5 1a6 6 0 0 0 2.5 2.5L7 6l3 1v2a1 1 0 0 1-1 1A9 9 0 0 1 1 2a1 1 0 0 1 1-1z" fill="#fff"/></svg><span>+61 2 5550 1473</span></li>
        <li><svg viewBox="0 0 11 11"><rect x="1" y="3" width="9" height="7" fill="#fff"/><rect x="3" y="1" width="5" height="3" fill="none" stroke="#fff"/></svg><span>+61 2 5550 1480</span></li>
        <li><svg viewBox="0 0 11 11"><circle cx="5.5" cy="5.5" r="4.5" fill="none" stroke="#fff"/><path d="M1 5.5h9M5.5 1c-2 3-2 6 0 9M5.5 1c2 3 2 6 0 9" fill="none" stroke="#fff" stroke-width="0.8"/></svg><span>www.<strong>zelvon</strong>.example</span></li>
        <li><svg viewBox="0 0 11 11"><rect x="0.5" y="2" width="10" height="7" fill="none" stroke="#fff"/><path d="M0.5 2l5 4 5-4" fill="none" stroke="#fff"/></svg><span>carla.mendoza@northquill.example</span></li>
      </ul>
    </div>
  </section>
</body>
</html>
```